Logo for Equipment and Auto parts seller
Crestline Supply and Machinery Corporation
Logo for Equipment and Auto parts seller - Automotive
Creative Brief
Simple
Julien Marceau
Operations Manager
Toliso
Julien.Marceau@cslmcorp.net

```html
<!DOCTYPE html>
<html lang="en">
<head>
<meta charset="utf-8">
<title>Crestline Supply and Machinery Corporation – Business Card</title>
<link href="https://fonts.googleapis.com/css2?family=Montserrat:wght@600;800&family=Open+Sans:wght@400;600;700&display=swap" rel="stylesheet">
<style>
  :root {
    --navy: #2e2a86;
    --green: #7cc242;
    --white: #ffffff;
    --paper: #fbfbfb;
    --backdrop: #7b7b7b;
    --ink-soft: #3b3b5a;
  }
  * { margin: 0; padding: 0; box-sizing: border-box; }
  html, body { width: 1200px; height: 908px; overflow: hidden; }
  body {
    background: var(--backdrop);
    font-family: "Open Sans", Arial, sans-serif;
    position: relative;
  }
  .card {
    position: absolute;
    top: 305px;
    width: 520px;
    height: 298px;
    border-radius: 16px;
    overflow: hidden;
  }
  .card-back { left: 50px; background: var(--navy); }
  .card-front { left: 630px; background: var(--paper); }

  /* brand lockup */
  .brand {
    display: flex;
    flex-direction: column;
    align-items: center;
    position: absolute;
  }
  .brand-row { display: flex; align-items: center; gap: 8px; }
  .brand-dot { width: 22px; height: 22px; border-radius: 50%; }
  .brand-initials {
    font-family: "Montserrat", Arial, sans-serif;
    font-weight: 800;
    font-size: 30px;
    letter-spacing: 1px;
    line-height: 1;
  }
  .brand-name {
    font-family: "Montserrat", Arial, sans-serif;
    font-weight: 800;
    font-size: 8.5px;
    letter-spacing: 0.6px;
    text-transform: uppercase;
    text-align: center;
    line-height: 1.35;
    margin-top: 6px;
    width: 190px;
  }

  .card-back .brand { left: 50%; top: 96px; transform: translateX(-50%); color: var(--white); }
  .card-back .brand-dot { background: var(--green); }

  .card-front .brand { left: 74px; top: 52px; color: var(--navy); }
  .card-front .brand-dot { background: var(--green); }

  .front-sweep { position: absolute; right: 0; top: 0; width: 200px; height: 298px; }

  .holder { position: absolute; left: 82px; top: 160px; }
  .holder-name { color: var(--navy); font-weight: 700; font-size: 17px; line-height: 1.2; }
  .holder-title { color: var(--green); font-weight: 600; font-size: 13px; line-height: 1.3; }

  .contact-list { position: absolute; left: 82px; top: 212px; list-style: none; color: var(--ink-soft); font-size: 11px; }
  .contact-list li { display: flex; align-items: center; gap: 6px; height: 17px; }
  .contact-list .plain { padding-left: 0; }
  .contact-icon { width: 12px; height: 12px; flex: none; }
</style>
</head>
<body>

  <section class="card card-back" aria-label="Card back">
    <div class="brand">
      <div class="brand-row">
        <span class="brand-dot"></span>
        <span class="brand-initials">CSMC</span>
      </div>
      <div class="brand-name">Crestline Supply and Machinery Corporation</div>
    </div>
  </section>

  <section class="card card-front" aria-label="Card front">
    <svg class="front-sweep" viewBox="0 0 200 298" aria-hidden="true">
      <circle cx="210" cy="128" r="122" fill="var(--green)"/>
      <path d="M200 28 C120 50 78 150 118 298 L146 298 C108 160 140 70 200 52 Z" fill="var(--navy)"/>
      <path d="M200 52 C140 70 108 160 146 298 L200 298 Z" fill="var(--paper)"/>
    </svg>

    <div class="brand">
      <div class="brand-row">
        <span class="brand-dot"></span>
        <span class="brand-initials">CSMC</span>
      </div>
      <div class="brand-name">Crestline Supply and Machinery Corporation</div>
    </div>

    <div class="holder">
      <div class="holder-name">Julien Marceau</div>
      <div class="holder-title">Operations Manager</div>
    </div>

    <ul class="contact-list">
      <li class="plain">Toliso</li>
      <li>
        <svg class="contact-icon" viewBox="0 0 12 12" aria-hidden="true">
          <circle cx="6" cy="6" r="6" fill="var(--green)"/>
          <path d="M4 3 L5.2 3 L5.6 4.6 L4.9 5.2 C5.3 6 6 6.7 6.8 7.1 L7.4 6.4 L9 6.8 L9 8 C9 8.5 8.6 9 8 9 C5.2 8.8 3.2 6.8 3 4 C3 3.4 3.5 3 4 3 Z" fill="var(--white)"/>
        </svg>
        +225 07 38 64 15
      </li>
      <li>
        <svg class="contact-icon" viewBox="0 0 12 12" aria-hidden="true">
          <circle cx="6" cy="6" r="6" fill="var(--green)"/>
          <rect x="3" y="3.8" width="6" height="4.4" rx="0.6" fill="none" stroke="var(--white)" stroke-width="0.9"/>
          <path d="M3.2 4.1 L6 6.2 L8.8 4.1" fill="none" stroke="var(--white)" stroke-width="0.9"/>
        </svg>
        Julien.Marceau@cslmcorp.net
      </li>
    </ul>
  </section>

</body>
</html>
```